Property casualty insurance consultant. Review business insurance plans and provide risk mgmt advice

Front side: logo, tag line, name and info
Back side: Services

Front:
Marcus T. Hollis
Property / Casualty Insurance Consulting and Training
P.O. Box 7385
Ashfield, NC 27890
marcus@brindlecrestpartners.example 336-555-0147 www.brindlecrestpartners.example
Back side:
Insurance Program Review
Renewal Proposal Review
Safety Planning / Loss Control
Disaster Planning
Claims Assistance
Updates

Images uploaded. I am non tech so let me know if this did not work. Choose image with Blue Fonts and Orange design element. The brief has also changed to put all info on front and services on back. Thank you.

Reason: took a while to get images downloaded

Going through elimination process. Thanks to all. On any revisions, please add two more services on reverse: Company Training . Agency Training

Target Market(s)

Business owners of all sizes and types

Industry/Entity Type

Insurance

Requirements
Must have
• Logo will have the colors to use, info fonts probably black and should closely match that in logo. Front side, logo, tag line, name and info. Back side with services and logo design element incorporated somehow

```html
<!DOCTYPE html>
<html lang="en">
<head>
<meta charset="utf-8">
<title>Brindlecrest Insurance Advisory – Business Cards</title>
<link href="https://fonts.googleapis.com/css2?family=Cinzel:wght@400;600&family=Open+Sans:wght@400;600&display=swap" rel="stylesheet">
<style>
  :root {
    --navy: #1f3a78;
    --blue: #3d64a0;
    --blue-deep: #2a4a88;
    --orange: #f07a1e;
    --amber: #f3a93a;
    --yellow: #efd21c;
    --paper: #fbfbfb;
    --stage: #e9e9ec;
    --white: #ffffff;
  }
  * { box-sizing: border-box; margin: 0; padding: 0; }
  html, body { width: 1200px; height: 800px; overflow: hidden; }
  body {
    background: var(--stage);
    font-family: "Open Sans", Arial, sans-serif;
    display: flex;
    align-items: center;
    justify-content: center;
    gap: 40px;
  }
  .card {
    width: 540px;
    height: 309px;
    position: relative;
    overflow: hidden;
    box-shadow: 0 6px 18px rgba(0,0,0,0.18);
  }

  /* ---------- Back: services ---------- */
  .card--back { background: linear-gradient(180deg, var(--blue) 0%, var(--blue-deep) 100%); }
  .services {
    position: absolute; left: 0; top: 0; width: 100%; height: 122px;
    background: linear-gradient(90deg, var(--orange) 0%, var(--amber) 55%, #e8c02a 100%);
    display: flex; gap: 40px;
    padding: 18px 28px 0 34px;
    color: var(--navy);
    font-size: 15px; line-height: 22px;
  }
  .services ul { list-style: none; }
  .services li::before { content: "\25CF"; font-size: 10px; margin-right: 7px; vertical-align: 2px; }
  .services__col--first { width: 260px; }
  .service-rules {
    position: absolute; left: 0; top: 122px; width: 100%; height: 7px;
    background: linear-gradient(180deg, #7fae3a 0 1px, var(--yellow) 1px 3px, var(--blue-deep) 3px 4px, var(--orange) 4px 6px, var(--blue) 6px 7px);
  }
  .back-mark {
    position: absolute; left: 0; right: 0; top: 185px;
    text-align: center; color: var(--white);
  }
  .wordmark { font-family: "Open Sans", Arial, sans-serif; font-weight: 600; letter-spacing: 2px; }
  .back-mark .wordmark { font-size: 30px; line-height: 38px; }
  .back-mark .wordmark small { display: block; font-size: 14px; letter-spacing: 6px; }

  /* ---------- Front: identity ---------- */
  .card--front { background: var(--paper); }
  .front-mark {
    position: absolute; right: 30px; top: 26px; text-align: right;
    color: var(--navy);
  }
  .front-mark .wordmark { font-size: 27px; line-height: 32px; }
  .front-mark .wordmark small { display: block; font-size: 12px; letter-spacing: 5px; }
  .identity { position: absolute; left: 30px; top: 104px; color: var(--blue); }
  .identity__name { font-family: "Cinzel", Georgia, serif; font-size: 20px; letter-spacing: 2px; font-weight: 400; }
  .identity__title { font-size: 12.5px; margin-top: 2px; }
  .front-rule {
    position: absolute; left: 0; top: 170px; width: 100%; height: 2px;
    background: linear-gradient(90deg, var(--orange), var(--yellow));
  }
  .contact-band {
    position: absolute; left: 0; bottom: 0; width: 100%; height: 137px;
    background: linear-gradient(180deg, var(--blue) 0%, var(--blue-deep) 100%);
    color: var(--white); font-size: 12.5px;
  }
  .contact-list { list-style: none; position: absolute; left: 30px; top: 16px; line-height: 21px; }
  .contact-list li { display: flex; align-items: center; gap: 8px; }
  .contact-list svg { width: 14px; height: 14px; flex: none; }
  .address { position: absolute; right: 30px; bottom: 18px; text-align: right; font-style: normal; font-size: 14px; line-height: 21px; }
</style>
</head>
<body>

  <section class="card card--back" aria-label="Business card back: services">
    <div class="services">
      <ul class="services__col services__col--first">
        <li>Insurance Program Review</li>
        <li>Renewal Proposal Review</li>
        <li>Safety Planning / Loss Control</li>
        <li>Disaster Planning</li>
      </ul>
      <ul class="services__col">
        <li>Claims Assistance</li>
        <li>Company Training</li>
        <li>Agency Training</li>
      </ul>
    </div>
    <div class="service-rules"></div>
    <div class="back-mark">
      <p class="wordmark">BRINDLECREST<small>INSURANCE ADVISORY</small></p>
    </div>
  </section>

  <section class="card card--front" aria-label="Business card front: contact">
    <div class="front-mark">
      <p class="wordmark">BRINDLECREST<small>INSURANCE ADVISORY</small></p>
    </div>
    <div class="identity">
      <h1 class="identity__name">MARCUS T. HOLLIS</h1>
      <p class="identity__title">Property | Casualty Insurance Consulting and Training</p>
    </div>
    <div class="front-rule"></div>
    <div class="contact-band">
      <ul class="contact-list">
        <li>
          <svg viewBox="0 0 14 14" aria-hidden="true"><rect width="14" height="14" rx="2" fill="#f3a93a"/><path d="M4 3.5c.5-.5 1-.4 1.3.1l.8 1.3c.2.4.1.8-.2 1l-.5.4c.4.9 1.2 1.7 2.1 2.1l.4-.5c.3-.3.7-.4 1-.2l1.3.8c.5.3.6.8.1 1.3-1 1-2.3.9-4.1-.6C4.5 7.8 3 5.7 4 3.5z" fill="#fff"/></svg>
          336-555-0147
        </li>
        <li>
          <svg viewBox="0 0 14 14" aria-hidden="true"><rect width="14" height="14" rx="2" fill="#f3a93a"/><rect x="3" y="4.2" width="8" height="5.6" fill="none" stroke="#fff" stroke-width="1"/><path d="M3 4.4l4 3 4-3" fill="none" stroke="#fff" stroke-width="1"/></svg>
          marcus@brindlecrestpartners.example
        </li>
        <li>
          <svg viewBox="0 0 14 14" aria-hidden="true"><rect width="14" height="14" rx="2" fill="#f3a93a"/><circle cx="7" cy="7" r="3.6" fill="none" stroke="#fff" stroke-width="1"/><path d="M3.4 7h7.2M7 3.4c-1.6 2-1.6 5.2 0 7.2M7 3.4c1.6 2 1.6 5.2 0 7.2" fill="none" stroke="#fff" stroke-width=".8"/></svg>
          www.brindlecrestpartners.example
        </li>
      </ul>
      <address class="address">P.O. Box 7385<br>Ashfield, NC 27890</address>
    </div>
  </section>

</body>
</html>
```